A new medical waste company needs an attractive and modern flyer.

We are a new medical waste company disposing of biohazards waste, red bag waste and sharps disposal with a focus on customer service.

Background Information

Company Name
Trovik Waste

Industry
Medical waste management

Description of the organization and its target audience

We are a new medical waste company disposing of biohazardous waste, red bag waste and medical sharps.

Description

MODERN & ELEGANT HALF PAGE FLYER

Half page mailer (front and back) with a large image related to the medical field.

The Trovik Waste logo, with the company tag line “compliant waste solutions” should also be on front of the mailer.

Website (trovikwaste.com) & email (info@trovikwatse.com) on both sides of the flyer

Main headline
-Now you have options for your medical waste disposal

Who we serve
- Dentist
- Physicians
-Blood banks
-Tattoo parlors
-Assisted living facilities
-Laboratories
-Veterinarians

What we offer
-Straight forward pricing
-No hidden fees
-No long term contracts
-Free containers and red bags
-Routine scheduled pickups

Price $35.95
Updates

Remember this is a half page flyer. Please remove pricing from all future work.

Target Market(s)

- Dentist
- Physicians
-Blood banks
-Tattoo parlors
-Laboratories
-Veterinarians

Industry/Entity Type

It Company

Colors
33b8a4

Requirements
Must have
• See my website www.trovikwaste.com

```html
<!DOCTYPE html>
<html lang="en">
<head>
<meta charset="utf-8">
<title>Trovik Waste – Medical Waste Disposal Flyer</title>
<link rel="stylesheet" href="https://fonts.googleapis.com/css2?family=Sorts+Mill+Goudy&family=Raleway:wght@400;600&family=Berkshire+Swash&display=swap">
<style>
  :root {
    --teal: #33b8a4;
    --teal-dark: #17695d;
    --teal-light: #7fd3c4;
    --teal-glass: rgba(110, 200, 180, 0.78);
    --ink: #1d2424;
    --brand-green: #2f7d32;
    --panel-top: #d6eef0;
    --panel-bottom: #eef7f7;
    --white: #ffffff;
    --rule: #9aa5a7;
  }
  * { box-sizing: border-box; margin: 0; padding: 0; }
  html, body { width: 1200px; height: 777px; overflow: hidden; background: var(--white); }
  .flyer { position: relative; width: 1200px; height: 777px; overflow: hidden; font-family: "Sorts Mill Goudy", Georgia, serif; color: var(--ink); }

  .hero-photo { position: absolute; left: 0; top: 0; width: 1200px; height: 272px;
    background: linear-gradient(100deg, #e4e7e8 0%, #f2f3f3 40%, #dfe3e4 70%, #eceeee 100%); }

  .brand { position: absolute; left: 36px; top: 70px; width: 390px; }
  .brand-name { display: flex; align-items: center; gap: 14px; font-family: "Raleway", Arial, sans-serif; font-weight: 600; font-size: 38px; letter-spacing: 0.5px; color: var(--ink); text-transform: uppercase; white-space: nowrap; }
  .brand-dot { width: 52px; height: 52px; border-radius: 50%; background: var(--brand-green); flex: none; }
  .brand-tagline { margin: 50px 0 0 32px; font-family: "Berkshire Swash", cursive; font-size: 27px; color: var(--ink); white-space: nowrap; }

  .headline-box { position: absolute; left: 446px; top: 84px; width: 714px; height: 108px; background: var(--teal-glass); border-radius: 3px; display: flex; align-items: center; justify-content: center; }
  .headline { color: var(--white); font-weight: 400; font-size: 35px; line-height: 42px; text-align: center; letter-spacing: 1px; }

  .content { position: absolute; left: 0; top: 272px; width: 1200px; height: 454px; background: linear-gradient(180deg, var(--panel-top), var(--panel-bottom)); }
  .section-title { position: absolute; font-family: "Raleway", Arial, sans-serif; font-weight: 400; font-size: 22px; letter-spacing: 1.5px; text-transform: uppercase; color: var(--ink); }
  .serve-title { left: 62px; top: 42px; }
  .offer-title { left: 620px; width: 400px; top: 42px; text-align: center; }

  .serve-list { position: absolute; left: 96px; top: 84px; list-style: none; }
  .serve-list li { display: flex; align-items: center; height: 47.2px; font-size: 20px; letter-spacing: 1.2px; }
  .serve-list svg { width: 14px; height: 12px; margin-right: 16px; }

  .divider { position: absolute; left: 420px; top: 46px; width: 1px; height: 362px; background: var(--rule); }

  .offer { position: absolute; width: 240px; text-align: center; }
  .offer svg { display: block; margin: 0 auto; width: 47px; height: 47px; }
  .offer-label { margin-top: 30px; font-size: 19.5px; line-height: 20px; letter-spacing: 1.4px; }

  .footer { position: absolute; left: 0; top: 726px; width: 1200px; height: 51px; background: var(--teal); color: var(--white); }
  .contact { position: absolute; top: 0; height: 51px; display: flex; align-items: center; gap: 12px; font-size: 22px; letter-spacing: 0.6px; }
  .contact svg { width: 14px; height: 14px; }
  .contact-web { left: 558px; }
  .contact-mail { left: 886px; }
</style>
</head>
<body>
<main class="flyer">
  <div class="hero-photo" role="img" aria-label="Photo of a doctor's desk from above: hands typing on a laptop, stethoscope, clipboard and glasses"></div>

  <div class="brand">
    <div class="brand-name"><span class="brand-dot"></span>Trovik Waste</div>
    <p class="brand-tagline">compliant waste solutions</p>
  </div>

  <div class="headline-box">
    <h1 class="headline">Now you have options for your medical<br>waste disposal</h1>
  </div>

  <section class="content">
    <h2 class="section-title serve-title">Who We Serve</h2>
    <ul class="serve-list">
      <li><svg viewBox="0 0 14 12"><path d="M1 6.5l4 4L13 1.5" fill="none" stroke="#33b8a4" stroke-width="2.6"/></svg>Dentist</li>
      <li><svg viewBox="0 0 14 12"><path d="M1 6.5l4 4L13 1.5" fill="none" stroke="#33b8a4" stroke-width="2.6"/></svg>Physicians</li>
      <li><svg viewBox="0 0 14 12"><path d="M1 6.5l4 4L13 1.5" fill="none" stroke="#33b8a4" stroke-width="2.6"/></svg>Blood banks</li>
      <li><svg viewBox="0 0 14 12"><path d="M1 6.5l4 4L13 1.5" fill="none" stroke="#33b8a4" stroke-width="2.6"/></svg>Tattoo parlors</li>
      <li><svg viewBox="0 0 14 12"><path d="M1 6.5l4 4L13 1.5" fill="none" stroke="#33b8a4" stroke-width="2.6"/></svg>Assisted living facilities</li>
      <li><svg viewBox="0 0 14 12"><path d="M1 6.5l4 4L13 1.5" fill="none" stroke="#33b8a4" stroke-width="2.6"/></svg>Laboratories</li>
      <li><svg viewBox="0 0 14 12"><path d="M1 6.5l4 4L13 1.5" fill="none" stroke="#33b8a4" stroke-width="2.6"/></svg>Veterinarians</li>
    </ul>

    <div class="divider"></div>

    <h2 class="section-title offer-title">What We Offer</h2>

    <div class="offer" style="left:442px; top:102px;">
      <svg viewBox="0 0 48 48"><circle cx="24" cy="24" r="24" fill="#33b8a4"/><circle cx="24" cy="24" r="15" fill="#17695d"/><text x="24" y="30" text-anchor="middle" font-family="Arial, sans-serif" font-weight="700" font-size="17" fill="#fff">$</text></svg>
      <p class="offer-label">Straight forward<br>pricing</p>
    </div>
    <div class="offer" style="left:702px; top:102px;">
      <svg viewBox="0 0 48 48"><circle cx="24" cy="24" r="24" fill="#33b8a4"/><circle cx="24" cy="24" r="15" fill="#17695d"/><text x="24" y="30" text-anchor="middle" font-family="Arial, sans-serif" font-weight="700" font-size="17" fill="#fff">$</text></svg>
      <p class="offer-label">No hidden fees</p>
    </div>
    <div class="offer" style="left:943px; top:102px;">
      <svg viewBox="0 0 48 48"><circle cx="24" cy="24" r="24" fill="#33b8a4"/><circle cx="24" cy="24" r="15" fill="#17695d"/><path d="M18 15h9l4 4v14H18z" fill="none" stroke="#fff" stroke-width="1.6"/><path d="M21 21h7M21 25h7M21 29h7" stroke="#fff" stroke-width="1.4"/></svg>
      <p class="offer-label">No long term<br>contracts</p>
    </div>
    <div class="offer" style="left:557px; top:279px;">
      <svg viewBox="0 0 48 48"><circle cx="24" cy="24" r="24" fill="#33b8a4"/><path d="M24 0a24 24 0 0 1 0 48z" fill="#7fd3c4" opacity="0.5"/><rect x="2" y="16" width="44" height="16" rx="3" fill="#17695d"/><text x="24" y="29" text-anchor="middle" font-family="Arial, sans-serif" font-weight="700" font-size="13" fill="#fff">FREE</text></svg>
      <p class="offer-label">Free containers and<br>red bags</p>
    </div>
    <div class="offer" style="left:842px; top:279px;">
      <svg viewBox="0 0 48 48"><circle cx="24" cy="24" r="24" fill="#33b8a4"/><circle cx="24" cy="24" r="15" fill="#17695d"/><circle cx="24" cy="24" r="9" fill="none" stroke="#fff" stroke-width="1.6"/><path d="M24 24l-3 5M24 24v-6" stroke="#fff" stroke-width="1.6"/></svg>
      <p class="offer-label">Routine scheduled<br>pickups</p>
    </div>
  </section>

  <footer class="footer">
    <div class="contact contact-web">
      <svg viewBox="0 0 14 14"><circle cx="7" cy="7" r="6" fill="none" stroke="#fff" stroke-width="1.2"/><path d="M1 7h12M7 1c-3 3.5-3 8.5 0 12M7 1c3 3.5 3 8.5 0 12" fill="none" stroke="#fff" stroke-width="1"/></svg>
      <span>www.trovikwaste.com</span>
    </div>
    <div class="contact contact-mail">
      <svg viewBox="0 0 14 14"><rect x="0.5" y="3" width="13" height="9" fill="#fff"/><path d="M0.5 3l6.5 5 6.5-5" fill="none" stroke="#33b8a4" stroke-width="1.2"/></svg>
      <span>info@trovikwatse.com</span>
    </div>
  </footer>
</main>
</body>
</html>
```